Lawn mowing business card design

We need a business card design for our lawn mowing and gardening business which is located in the Northern Beaches of Sydney. Our business name is Meadowline Turf and our logo is predominantly green and yellow in color. Please see our website at www.meadowlineturf.com.au for design ideas. The business targets young professionals and older clientele. As such the font should be easy to read, but I also want the business card to be colorful and stand out.

Target Market(s)

young professionals

Industry/Entity Type

Lawn Care

Contact Information for Business Card

Meadowline Turf, Gareth Pellow, 0478559201, www.meadowlineturf.com.au, email: meadowlineturf@mailbox-example.com

Font styles to use
Serif

Colors
9bcb3b
fbed22

Requirements
Must have
• Must include the details listed above. Must include the attached logo.
Nice to have
• Logo attached with two copies. The logo without any writing is high quality, please feel free to be creative with the text stating our business name "Meadowline Turf" using this file.

```html
<!DOCTYPE html>
<html lang="en">
<head>
<meta charset="utf-8">
<title>Meadowline Turf — Business Card</title>
<link href="https://fonts.googleapis.com/css2?family=PT+Sans:wght@400;700&display=swap" rel="stylesheet">
<style>
  :root {
    --canvas-bg: #e9e9e9;
    --card-white: #ffffff;
    --leaf: #8cc63f;
    --leaf-dark: #5a8a2a;
    --leaf-deep: #3f6b1c;
    --sun: #f5d80f;
    --ink: #1f2a33;
    --soil: #4a3426;
    --shadow: rgba(0, 0, 0, 0.18);
  }
  html, body {
    margin: 0;
    padding: 0;
    width: 1200px;
    height: 1095px;
    overflow: hidden;
    background: var(--canvas-bg);
    font-family: "PT Sans", sans-serif;
  }
  .canvas {
    position: relative;
    width: 1200px;
    height: 1095px;
  }
  .card {
    position: absolute;
    top: 168px;
    width: 440px;
    height: 760px;
    box-shadow: 0 18px 40px var(--shadow);
    background: var(--card-white);
  }
  .card--front { left: 120px; }
  .card--back { left: 640px; }
  .card svg { display: block; width: 440px; height: 760px; }
  .brand-name { font-family: "PT Sans", sans-serif; font-weight: 700; fill: var(--leaf-dark); }
  .person-first { font-weight: 700; fill: var(--leaf); }
  .person-last { font-weight: 400; fill: var(--leaf-dark); }
  .contact-text { font-family: "PT Sans", sans-serif; fill: var(--card-white); font-size: 20px; }
  .contact-badge { fill: var(--ink); }
  .contact-icon { fill: none; stroke: var(--card-white); stroke-width: 2; }
  .back-title { font-family: "PT Sans", sans-serif; font-weight: 700; fill: var(--leaf); }
  .back-tagline, .back-phone { font-family: "PT Sans", sans-serif; fill: var(--sun); }
</style>
</head>
<body>
<main class="canvas">

  <!-- Front: name and contact details -->
  <section class="card card--front" aria-label="Business card front">
    <svg viewBox="0 0 440 760" xmlns="http://www.w3.org/2000/svg">
      <rect width="440" height="760" fill="var(--card-white)"/>

      <g class="brand-mark">
        <circle cx="92" cy="160" r="16" fill="var(--leaf)"/>
        <text class="brand-name" x="120" y="172" font-size="36">Meadowline Turf</text>
      </g>

      <text x="52" y="318" font-family="PT Sans, sans-serif" font-size="34">
        <tspan class="person-first">Gareth</tspan>
        <tspan class="person-last">Pellow</tspan>
      </text>

      <g class="ribbon">
        <polygon points="0,400 300,400 440,440 440,640 0,760" fill="var(--leaf)"/>
        <polygon points="300,348 372,342 440,396 440,440 300,400" fill="var(--leaf-dark)"/>
      </g>

      <g class="contact contact--phone">
        <polygon class="contact-badge" points="52,450 70,460 70,482 52,492 34,482 34,460"/>
        <rect class="contact-icon" x="46" y="461" width="12" height="20" rx="2"/>
        <text class="contact-text" x="86" y="478">0478 559 201</text>
      </g>
      <g class="contact contact--email">
        <polygon class="contact-badge" points="52,520 70,530 70,552 52,562 34,552 34,530"/>
        <rect class="contact-icon" x="43" y="534" width="18" height="13" rx="1"/>
        <polyline class="contact-icon" points="43,535 52,542 61,535"/>
        <text class="contact-text" x="86" y="548" font-size="17">meadowlineturf@mailbox-example.com</text>
      </g>
      <g class="contact contact--web">
        <polygon class="contact-badge" points="52,590 70,600 70,622 52,632 34,622 34,600"/>
        <circle class="contact-icon" cx="52" cy="611" r="9"/>
        <line class="contact-icon" x1="43" y1="611" x2="61" y2="611"/>
        <ellipse class="contact-icon" cx="52" cy="611" rx="4" ry="9"/>
        <text class="contact-text" x="86" y="618">www.meadowlineturf.com.au</text>
      </g>
    </svg>
  </section>

  <!-- Back: brand panel -->
  <section class="card card--back" aria-label="Business card back">
    <svg viewBox="0 0 440 760" xmlns="http://www.w3.org/2000/svg">
      <rect width="440" height="760" fill="var(--card-white)"/>

      <g class="folds">
        <polygon points="160,50 410,40 410,140 160,175" fill="var(--leaf-dark)"/>
        <polygon points="160,175 410,140 440,250 0,270" fill="var(--leaf)"/>
        <polygon points="0,270 440,250 440,330 0,320" fill="var(--leaf-dark)"/>
        <polygon points="0,320 440,330 440,460 0,470" fill="var(--leaf)"/>
      </g>

      <circle class="brand-seal" cx="220" cy="400" r="72" fill="var(--card-white)" stroke="var(--leaf-deep)" stroke-width="2"/>

      <text class="back-title" x="220" y="545" font-size="38" text-anchor="middle">MEADOWLINE TURF</text>
      <text class="back-tagline" x="220" y="580" font-size="20" text-anchor="middle">Lawn and Garden Maintenance</text>
      <text class="back-phone" x="220" y="612" font-size="20" text-anchor="middle">0478 559 201</text>

      <defs>
        <linearGradient id="turf-fade" x1="0" y1="0" x2="0" y2="1">
          <stop offset="0" stop-color="#ffffff"/>
          <stop offset="1" stop-color="#7fbf3a"/>
        </linearGradient>
      </defs>
      <rect class="turf-strip" x="0" y="630" width="440" height="70" fill="url(#turf-fade)" role="img" aria-label="Strip of grass blades along the lower edge"/>
      <rect class="soil-strip" x="0" y="700" width="440" height="60" fill="var(--soil)"/>
    </svg>
  </section>

</main>
</body>
</html>
```